Visitenkarte für Ergotherapiepraxis
Zielgruppe
Wir arbeiten mit Kindern und Erwachsene jeden Alters.
Diese Personen kommen mit Beeinträchtigungen (körperlich, seelisch, schulisch) im täglichen Leben zu uns. Wir unterstützen unsere Patienten die Beeinträchtigungen zu verringern oder zu kompensieren und so den Alltag besser bewältigen zu können.
Aufgabenstellung
Ein Design was Kinder und Erwachsene anspricht, aber nicht zu verspielt wirkt. Es soll vertrauenserweckend sein. Eventuell sollte die Visitenkarte ein "aufgehendes oder erblühendes oder aufsteigendes" Element enthalten (=zu Beginn war die Beeinträchtigung dann steigt die Lebensqualität als Folge der Behandlung)
Daten vorn:
Ergotherapiepraxis

```html
<!DOCTYPE html>
<html lang="de">
<head>
<meta charset="utf-8">
<title>Visitenkarte Ergotherapiepraxis</title>
<link rel="stylesheet" href="https://fonts.googleapis.com/css2?family=Sacramento&family=Roboto+Condensed:wght@300&display=swap">
<style>
  :root {
    --backdrop: #f1f1f0;
    --card: #ffffff;
    --ink: #3a3a3a;
    --blossom: #e0568a;
    --blossom-mid: rgba(224, 86, 138, 0.55);
    --blossom-soft: rgba(243, 179, 203, 0.3);
    --clear: rgba(255, 255, 255, 0);
  }
  * { margin: 0; padding: 0; box-sizing: border-box; }
  html, body { width: 1200px; height: 847px; overflow: hidden; }
  body {
    background: var(--backdrop);
    position: relative;
    font-family: "Roboto Condensed", "Arial Narrow", sans-serif;
    color: var(--ink);
  }
  .card {
    position: absolute;
    top: 238px;
    width: 484px;
    height: 317px;
    background: var(--card);
    box-shadow: 0 2px 6px rgba(0,0,0,0.12);
    overflow: hidden;
  }
  .card--front { left: 111px; }
  .card--back { left: 615px; }

  .blossom-art {
    position: absolute;
    background: radial-gradient(ellipse closest-side at 50% 50%,
      var(--blossom) 0%, var(--blossom-mid) 40%, var(--blossom-soft) 70%, var(--clear) 100%);
  }
  .card--front .blossom-art { left: 262px; top: -30px; width: 260px; height: 300px; }
  .card--back .blossom-art { left: 200px; top: -50px; width: 320px; height: 200px; }

  .bird-art {
    position: absolute;
    left: 52px; top: 138px;
    width: 64px; height: 68px;
    background: radial-gradient(circle closest-side at 50% 50%,
      var(--blossom) 0%, var(--blossom-mid) 50%, var(--clear) 100%);
  }

  .name {
    font-family: "Sacramento", cursive;
    font-weight: 400;
    color: var(--ink);
    white-space: nowrap;
    line-height: 1;
  }
  .card--front .name {
    position: absolute;
    left: 26px; top: 40px;
    font-size: 34px;
  }
  .practice {
    position: absolute;
    left: 28px; top: 80px;
    font-size: 18px;
    font-weight: 300;
    letter-spacing: 2px;
  }
  .contact {
    position: absolute;
    left: 28px; top: 132px;
    font-size: 17px;
    font-weight: 300;
    letter-spacing: 1px;
    line-height: 26.5px;
    font-style: normal;
  }

  .therapist-label {
    position: absolute;
    left: 135px; top: 184px;
    font-size: 17px;
    font-weight: 300;
    letter-spacing: 0.8px;
  }
  .card--back .name {
    position: absolute;
    left: 150px; top: 230px;
    width: 190px;
    text-align: center;
    font-size: 32px;
  }
</style>
</head>
<body>
  <section class="card card--front">
    <div class="blossom-art" role="img" aria-label="Blühender Kirschzweig mit rosa Blüten und einem sitzenden Vogel"></div>
    <h1 class="name">Marlene Brandt</h1>
    <p class="practice">Ergotherapiepraxis</p>
    <address class="contact">
      Am Lindenhof 4<br>
      14712 Feldheim, OT Weide<br>
      Tel. 033845/71904
    </address>
  </section>

  <section class="card card--back">
    <div class="blossom-art" role="img" aria-label="Kirschzweig mit rosa Blüten an der oberen rechten Ecke"></div>
    <div class="bird-art" role="img" aria-label="Rosa auffliegender Vogel"></div>
    <p class="therapist-label">Behandelnder Therapeut:</p>
    <p class="name">Marlene Brandt</p>
  </section>
</body>
</html>
```